Letterhead Design Needed for Real Estate Office

We are a boutique real estate agency focused on property management. We need a letter head which is professional looking and include the following information:

Logo
ABN Number
Address
Postal Address
Phone
Fax
Mobile
Email
Website

Please note that the PLVAQT logo can not be changed and must be positioned at the bottom right corner.

Please find attached the existing letterhead design for all the required elements.

Target Market(s)

Letterhead mostly used for service of notices, business letters, clients communication

Industry/Entity Type

Boutique

Colors

Designer to choose colors to be used in the design.

Requirements
Must have
• Logo

```html
<!DOCTYPE html>
<html lang="en">
<head>
<meta charset="utf-8">
<title>Halvard Partners Letterhead</title>
<link rel="stylesheet" href="https://fonts.googleapis.com/css2?family=Arimo:wght@400;700&display=swap">
<style>
  :root {
    --navy: #1c3a6b;
    --swoosh: #ececec;
    --brand-green: #5a9a2a;
    --ink: #3a3a3a;
    --paper: #ffffff;
  }
  html, body {
    margin: 0;
    padding: 0;
    overflow: hidden;
    background: var(--paper);
  }
  .letterhead {
    position: relative;
    width: 889px;
    height: 1200px;
    overflow: hidden;
    background: var(--paper);
    font-family: "Arimo", Arial, sans-serif;
  }
  .backdrop {
    position: absolute;
    inset: 0;
  }
  .brand {
    position: absolute;
    left: 34px;
    top: 40px;
    display: flex;
    align-items: center;
    gap: 12px;
  }
  .brand-mark {
    width: 34px;
    height: 34px;
    background: var(--brand-green);
  }
  .brand-name {
    font-weight: 700;
    font-size: 26px;
    letter-spacing: 1px;
    color: var(--brand-green);
  }
  .membership {
    position: absolute;
    right: 40px;
    top: 1075px;
    font-weight: 700;
    font-size: 34px;
    letter-spacing: 1px;
    color: var(--navy);
  }
  .footer {
    position: absolute;
    left: 0;
    right: 0;
    top: 1158px;
    height: 42px;
    background: var(--navy);
    color: var(--paper);
    font-size: 9.5px;
    line-height: 14px;
    text-align: center;
    padding-top: 7px;
    box-sizing: border-box;
  }
  .footer b { font-weight: 700; }
</style>
</head>
<body>
<div class="letterhead">
  <svg class="backdrop" width="889" height="1200" viewBox="0 0 889 1200" aria-hidden="true">
    <rect x="0" y="0" width="889" height="4" fill="var(--navy)"/>
    <path d="M0 4 H889 V18 C700 22 520 55 390 105 C300 140 150 160 0 152 Z" fill="var(--swoosh)"/>
    <path d="M0 1158 C200 1152 350 1105 500 1072 C630 1046 770 1034 889 1040 V1158 Z" fill="var(--swoosh)"/>
  </svg>

  <header class="brand">
    <div class="brand-mark"></div>
    <div class="brand-name">HALVARD PARTNERS</div>
  </header>

  <div class="membership">PLVAQT</div>

  <footer class="footer">
    <div><b>ABN</b> 48 302 715 609 | Shop 12b 218-230 Ashby Road Lindfield NSW 2070 AUSTRALIA | PO BOX 415 Lindfield NSW 2070</div>
    <div><b>m</b> 0400 123 456 | <b>p</b> 9555 0142 | <b>f</b> 95550143 | <b>e</b> hello@halvardpr.com | <b>w</b> http://halvardpr.com</div>
  </footer>
</div>
</body>
</html>
```